Rollup Display Poster Design Layout

We need 4 roll-up banner designs, 1 for each division of our company: (See required specification sheet attached)
-Divisions:
1- Electrical Contracting (yellow)
2- Security & Access Control (red)
3- Telecommunication Cabling (green)
4- Building Automation & Controls (blue)
See attached logos, there are 4 logos in total, one representing each division of our company by "Color"; see notation above to the right of each division name.
Each banner is to have 4 pictures laid out vertically stacked one on-top of each other filling up the full length of the banner which has a high of 97"
The file names for the various pictures which include the division name followed by a number (1 thur 4) indicating the preferable order in which they should be placed. However feel free to use your judgement to rearrange them.
The division name and # with be followed by a - and a "phase" such as "Generators". This second word following the division name should be superimposed on its respective picture on the banner.
The division's logo should be layout along top of the banner and taking up the full width which is 33" minus the margin.
Thank you for your consideration on this project!
Target Market(s)
Property Management, Property Owners
Industry/Entity Type
Electrical
Colors
Designer to choose colors to be used in the design.
Look and feel
Each slider illustrates characteristics of the customer's brand and the style your logo design should communicate.

```html
<!DOCTYPE html>
<html lang="en">
<head>
<meta charset="utf-8">
<title>Vanta Electric – Telecommunication Cabling Roll-up</title>
<link href="https://fonts.googleapis.com/css2?family=Roboto+Condensed:wght@400;700&display=swap" rel="stylesheet">
<style>
  :root {
    --brand-green: #7ba23a;
    --ink: #1f1f1f;
    --paper: #ffffff;
    --stage: #d9d9d9;
  }
  html, body {
    margin: 0;
    width: 1200px;
    height: 1200px;
    overflow: hidden;
    background: var(--stage);
  }
  .rollup {
    position: absolute;
    left: 382px;
    top: 30px;
    width: 435px;
    height: 1140px;
    background: var(--paper);
  }
  .rollup svg { display: block; width: 100%; height: 100%; }
  .type { font-family: "Roboto Condensed", "Arial Narrow", sans-serif; }
  .brand-name { font-weight: 700; font-size: 25px; fill: var(--ink); letter-spacing: 0.5px; }
  .brand-tag { font-weight: 700; font-size: 8.6px; fill: var(--ink); letter-spacing: 0.4px; }
  .service-label { font-weight: 700; font-size: 19px; fill: var(--paper); }
  .side-service { font-weight: 700; font-size: 21px; fill: var(--ink); }
  .headline { font-weight: 700; font-size: 49px; fill: var(--ink); }
  .subhead { font-weight: 700; font-size: 38px; fill: var(--ink); }
  .contact { font-weight: 700; font-size: 21px; fill: var(--ink); }
  .green { fill: var(--brand-green); }
  .dark { fill: var(--ink); }
</style>
</head>
<body>
<main class="rollup">
  <svg viewBox="0 0 491 1288" xmlns="http://www.w3.org/2000/svg">
    <defs>
      <linearGradient id="closetTone" x1="0" y1="0" x2="1" y2="1">
        <stop offset="0" stop-color="#8a8690"/>
        <stop offset="0.5" stop-color="#a6927a"/>
        <stop offset="1" stop-color="#6b5844"/>
      </linearGradient>
      <linearGradient id="cableTone" x1="0" y1="0" x2="1" y2="0">
        <stop offset="0" stop-color="#f3eef6"/>
        <stop offset="0.5" stop-color="#f7f1ee"/>
        <stop offset="1" stop-color="#f2f0f7"/>
      </linearGradient>
      <linearGradient id="techTone" x1="0" y1="0" x2="1" y2="1">
        <stop offset="0" stop-color="#3a4a7a"/>
        <stop offset="0.55" stop-color="#3f8f86"/>
        <stop offset="1" stop-color="#76c9c8"/>
      </linearGradient>
      <linearGradient id="panelTone" x1="0" y1="0" x2="1" y2="1">
        <stop offset="0" stop-color="#5a6fa8"/>
        <stop offset="1" stop-color="#a8a9d6"/>
      </linearGradient>
    </defs>

    <!-- Brand header -->
    <g class="brand type">
      <rect x="38" y="36" width="28" height="28" class="green"/>
      <text x="80" y="57" class="brand-name">VANTA ELECTRIC LLC</text>
      <text x="80" y="70" class="brand-tag">DATA/TELECOMMUNICATIONS CONTRACTORS</text>
    </g>

    <!-- Service photo: colourful patch cables -->
    <polygon points="0,384 247,285 491,155 491,420 0,704" fill="url(#cableTone)" role="img" aria-label="Photo: row of colourful RJ45 patch cables in black, red, yellow, purple, pink and green"/>

    <!-- Service photo: network closet -->
    <polygon points="0,148 262,218 0,384" fill="url(#closetTone)" role="img" aria-label="Photo: miniature workers inspecting a network patch cable in a server closet"/>
    <polygon points="0,122 280,196 268,222 0,150" class="green"/>
    <text class="service-label type" transform="translate(8,144) rotate(14.5)">NETWORK CLOSET DESIGN</text>

    <!-- Right accent stripes -->
    <polygon points="286,222 491,103 491,125 286,240" class="green"/>
    <polygon points="247,263 491,130 491,155 247,285" class="dark"/>
    <text x="451" y="284" text-anchor="end" class="side-service type">FIBER</text>
    <text x="451" y="313" text-anchor="end" class="side-service type">OPTIC</text>
    <text x="451" y="342" text-anchor="end" class="side-service type">CABLING</text>

    <!-- Service photo: technician at control panel -->
    <polygon points="0,704 491,452 491,828 430,850 0,742" fill="url(#techTone)" role="img" aria-label="Photo: technician testing wiring inside an electronic control cabinet"/>
    <polygon points="372,478 491,418 491,440 390,490" fill="#3aa5d8"/>
    <polygon points="420,436 491,418 491,470" class="dark"/>
    <polygon points="0,657 250,519 262,546 0,689" class="dark"/>
    <polygon points="0,689 256,548 262,560 0,704" class="green"/>
    <polygon points="240,560 275,552 252,584" fill="#f2d21c"/>
    <text class="service-label type" transform="translate(28,666) rotate(-29)">MAINTENANCE &amp; TESTING</text>

    <!-- Service photo: structured cabling patch panel -->
    <polygon points="0,738 429,853 0,1018" fill="url(#panelTone)" role="img" aria-label="Photo: patch panel with lavender network cables and a blue network switch"/>
    <polygon points="180,770 230,746 491,828 491,843 429,853" class="green"/>
    <polygon points="0,723 430,842 420,872 0,753" class="dark"/>
    <polygon points="344,903 491,843 491,1008" class="green"/>
    <text class="service-label type" transform="translate(110,776) rotate(15.5)">STRUCTURED CABLING</text>

    <!-- Headline -->
    <text x="246" y="1058" text-anchor="middle" class="headline type">TELECOMMUNICATION</text>
    <text x="246" y="1106" text-anchor="middle" class="subhead type">CABLING</text>

    <!-- Contact -->
    <g class="contact-phone">
      <circle cx="124" cy="1168" r="23" class="green"/>
      <path d="M114 1156 q-4 4 0 12 q6 11 16 16 q7 3 11 -1 l-5 -6 q-3 2 -6 0 q-6 -4 -9 -10 q-2 -3 1 -5 z" class="dark"/>
      <text x="117" y="1226" text-anchor="middle" class="contact type">123456 4789</text>
    </g>
    <g class="contact-web">
      <circle cx="356" cy="1168" r="23" class="green"/>
      <circle cx="356" cy="1168" r="15" fill="none" stroke="#1f1f1f" stroke-width="2"/>
      <ellipse cx="356" cy="1168" rx="6" ry="15" fill="none" stroke="#1f1f1f" stroke-width="2"/>
      <line x1="341" y1="1168" x2="371" y2="1168" stroke="#1f1f1f" stroke-width="2"/>
      <text x="351" y="1226" text-anchor="middle" class="contact type">YOURWEBSITE.COM</text>
    </g>
  </svg>
</main>
</body>
</html>
```